Business Card Design for Pastor/Church Leadership - simple, elegant, "different"

Design a name card based on logo and color from our branding guide - see file "MBF Logo and Color".
The teal frame around the logo is not part of the logo and is a not necessary design element for the name card (as the attached PDF file may suggest).
The font suggested by branding is "Frutiger 55 Roman".
The file "not good.pdf", a sample of a name card that is NOT good.
- fonts too small to read
- the tagline on the logo "Still waters, open door" not easy to read with logo used in this design
- "MAPLE GROVE FELLOWSHIP" unnecessarily duplicated - possibly because logo too small
- not sure about the green frame, probably better to drop

Target Market(s)

broad, all people the pastor of an international church in Tokyo meets

Industry/Entity Type

Business

Contact Information for Business Card

Mattias R. Pellworth
Pastor
3-9-4 Kawaranodai, Aozora-ku
Tokyo 162-0048 (Church)
2-21 Ochibamachi, Aozora-ku
Tokyo 162-0073 (Home)
Tel: 03-5817-2963
E-mail: pastor@maplegrovefell.org
URL: http://www.maplegrovefell.org

Font styles to use
Sans Serif
Other font styles liked:
• Frutiger 55 Roman (want, not must)

Requirements
Must have
• must include logo
• must make use of the "bright turquoise color"
• Cyan = 59, Magenta = 0, Yellow=24, Black=0
• Red=3.1%, Green=91%, Blue=87.1%
• Key Info (name) must be easy to read (see notes on bad sample namecard attached)

```html
<!DOCTYPE html>
<html lang="en">
<head>
<meta charset="utf-8">
<title>Maple Grove Fellowship – Pastor Business Card</title>
<link rel="stylesheet" href="https://fonts.googleapis.com/css2?family=Noto+Sans:wght@400;500&display=swap">
<style>
  :root {
    --page-bg: #e9e7e4;
    --card-teal: #72c6ca;
    --card-teal-light: #7fccd0;
    --ink-white: #ffffff;
    --ink-dark: #4a4f52;
    --card-shadow: rgba(0, 0, 0, 0.18);
  }
  * { margin: 0; padding: 0; box-sizing: border-box; }
  html, body {
    width: 1200px; height: 902px; overflow: hidden;
    background: var(--page-bg);
    font-family: "Noto Sans", "Frutiger", sans-serif;
  }
  .card {
    position: absolute;
    left: 150px; top: 179px;
    width: 900px; height: 544px;
    background: linear-gradient(135deg, var(--card-teal-light) 0%, var(--card-teal) 60%);
    box-shadow: 0 12px 34px var(--card-shadow);
    color: var(--ink-white);
  }
  .brand {
    position: absolute; left: 60px; top: 60px; width: 300px;
    text-align: center;
  }
  .brand-mark {
    display: flex; align-items: center; justify-content: center; gap: 14px;
    height: 130px;
    font-size: 56px; font-weight: 500; letter-spacing: 4px;
  }
  .brand-dot {
    width: 22px; height: 22px; border-radius: 50%;
    background: var(--ink-white);
  }
  .brand-name {
    margin-top: 18px;
    font-size: 18px; letter-spacing: 1.5px;
    padding-bottom: 8px;
    border-bottom: 2px solid var(--ink-white);
  }
  .brand-tagline { margin-top: 8px; font-size: 18px; }
  .church-address {
    position: absolute; left: 86px; top: 312px;
    display: flex; gap: 26px;
    font-size: 22px; line-height: 1.2; font-style: normal;
  }
  .icon { flex: none; }
  .person {
    position: absolute; left: 440px; top: 48px; width: 420px;
    text-align: center;
  }
  .person-name { font-size: 34px; font-weight: 400; color: var(--ink-dark); }
  .person-role { font-size: 28px; color: var(--ink-white); margin-top: 2px; }
  .contact {
    position: absolute; left: 480px; top: 222px;
    list-style: none; color: var(--ink-dark);
    font-size: 20px; line-height: 1.2;
  }
  .contact li { display: flex; gap: 18px; margin-bottom: 18px; align-items: flex-start; }
  .contact .icon { width: 24px; margin-top: 1px; }
  .website {
    position: absolute; left: 0; right: 0; bottom: 36px;
    text-align: center; font-size: 21px;
  }
</style>
</head>
<body>
  <article class="card">
    <header class="brand">
      <div class="brand-mark"><span class="brand-dot"></span>MBF</div>
      <p class="brand-name">MAPLE GROVE FELLOWSHIP</p>
      <p class="brand-tagline">Still waters, open door</p>
    </header>

    <address class="church-address">
      <svg class="icon" width="18" height="26" viewBox="0 0 18 26" aria-hidden="true">
        <path d="M9 1C4.6 1 1 4.5 1 8.9 1 14.8 9 25 9 25s8-10.2 8-16.1C17 4.5 13.4 1 9 1z" fill="none" stroke="#fff" stroke-width="2"/>
        <circle cx="9" cy="9" r="3" fill="#fff"/>
      </svg>
      <span>3-9-4 Kawaranodai<br>Aozora-ku<br>Tokyo 162-0048</span>
    </address>

    <section class="person">
      <h1 class="person-name">Mattias R. Pellworth</h1>
      <p class="person-role">Pastor</p>
    </section>

    <ul class="contact">
      <li>
        <svg class="icon" viewBox="0 0 24 26" height="26" aria-hidden="true">
          <rect x="5" y="1" width="14" height="24" rx="2.5" fill="none" stroke="#4a4f52" stroke-width="2"/>
          <line x1="10" y1="21" x2="14" y2="21" stroke="#4a4f52" stroke-width="2"/>
        </svg>
        <span>03-5817-2963</span>
      </li>
      <li>
        <svg class="icon" viewBox="0 0 24 18" height="18" aria-hidden="true">
          <rect x="1" y="1" width="22" height="16" fill="#4a4f52"/>
          <path d="M1 1l11 9 11-9" fill="none" stroke="#72c6ca" stroke-width="1.6"/>
        </svg>
        <span>pastor@maplegrovefell.org</span>
      </li>
      <li>
        <svg class="icon" viewBox="0 0 24 26" height="26" aria-hidden="true">
          <path d="M12 1C7.6 1 4 4.5 4 8.9 4 14.8 12 25 12 25s8-10.2 8-16.1C20 4.5 16.4 1 12 1z" fill="#4a4f52"/>
          <circle cx="12" cy="9" r="3" fill="#72c6ca"/>
        </svg>
        <span>2-21 Ochibamachi<br>Aozora-ku<br>Tokyo 162-0073</span>
      </li>
    </ul>

    <p class="website">http://www.maplegrovefell.org</p>
  </article>
</body>
</html>
```